Waterproofing Construction company needs letterhead

I need a letterhead design for a commercial waterproofing construction company. We would like to see designs that are contemporary, clean, sleek and use our logo. Our current design is dated. I would also like a cover page (see example) that goes with our letterhead. I would like for the footer to have our address, website, and phone number

Target Market(s)

Customers, potential customers.

Font styles to use
Sans Serif

Requirements
Must have
• logo, website, address, phone numbers, only our colors, tahoma font
• PMS: 295C PMS: 2995C
• CMYK: 100/84/36/39 CMYK: 80/12/1/0
• RGB: 16/44/82 RGB: 0/167/224
• HEX#: #102C52 HEX#: #00A7E0
• Black & White: 100% Black & White: 32%
• Gray Scale: 90% Gray Scale: 32%
Nice to have
• Our "icon" logo attached would be nice somewhere on the page.

```html
<!DOCTYPE html>
<html lang="en">
<head>
<meta charset="utf-8">
<title>Tidewall Letterhead</title>
<link rel="stylesheet" href="https://fonts.googleapis.com/css2?family=Lato:ital,wght@0,300;0,400;0,700;1,400&display=swap">
<style>
  :root {
    --navy: #102C52;
    --cyan: #00A7E0;
    --paper: #ffffff;
    --backdrop: #d8d1cf;
    --body-grey: #7a7a7a;
    --ink: #3a3a3a;
  }
  * { box-sizing: border-box; margin: 0; padding: 0; }
  html, body {
    width: 1200px;
    height: 784px;
    overflow: hidden;
    background: var(--backdrop);
    font-family: "Lato", sans-serif;
  }
  .letterhead {
    position: absolute;
    left: 317px;
    top: 26px;
    width: 566px;
    height: 732px;
    background: var(--navy);
    padding: 9px 9px 0 9px;
  }
  .letterhead__sheet {
    position: relative;
    width: 100%;
    height: 610px;
    background: var(--paper);
    padding: 34px 38px 0 38px;
  }
  .brand {
    position: absolute;
    top: 30px;
    right: 36px;
    display: flex;
    align-items: center;
    gap: 8px;
  }
  .brand__name {
    font-weight: 700;
    font-size: 30px;
    letter-spacing: 0.5px;
    color: var(--navy);
  }
  .brand__mark {
    width: 14px;
    height: 14px;
    background: var(--cyan);
  }
  .letter {
    position: absolute;
    top: 104px;
    left: 38px;
    right: 40px;
    color: var(--body-grey);
    font-size: 10.5px;
    line-height: 1.5;
    font-weight: 300;
  }
  .letter__salutation {
    font-style: italic;
    font-weight: 400;
    color: var(--ink);
    font-size: 11.5px;
    margin-bottom: 16px;
  }
  .letter__paragraph { margin-bottom: 14px; }
  .signoff {
    margin-top: 26px;
    color: var(--ink);
  }
  .signoff__closing {
    font-style: italic;
    font-size: 11.5px;
    margin-bottom: 10px;
  }
  .signoff__name {
    font-weight: 700;
    font-size: 12.5px;
    color: var(--ink);
  }
  .signoff__title {
    font-size: 8.5px;
    font-weight: 400;
    margin-bottom: 8px;
  }
  .signoff__signature {
    width: 110px;
    height: 22px;
    background: linear-gradient(90deg, #e2e2e2, #f1f1f1);
  }
  .footer {
    position: absolute;
    left: 0;
    right: 0;
    bottom: 0;
    height: 113px;
    padding: 24px 30px 0 30px;
    color: #ffffff;
    font-size: 11px;
    line-height: 1.55;
    font-weight: 400;
  }
  .footer__line { white-space: nowrap; }
</style>
</head>
<body>
  <main class="letterhead">
    <section class="letterhead__sheet">
      <header class="brand">
        <span class="brand__name">TIDEWALL</span>
        <span class="brand__mark"></span>
      </header>

      <article class="letter">
        <p class="letter__salutation">Dear sir/Madam,</p>
        <p class="letter__paragraph">Lorem ipsum dolor sit amet, an vel recteque dissentiet, detracto albucius platonem ex vel, eros repudiandae cu. Accu aliquando nec an, unum graece adolescens vel ad. Id odio scae has, iudico euismod atomorum ius ea, cum ea honestatis quaerendum theophrastus. Mea honestatis quaerendum theophrastus. Mea</p>
        <p class="letter__paragraph">Lorem ipsum dolor sit amet, an vel recteque dissentiet, detracto albucius platonem ex vel, eros repudiandae cu. Accu aliquando nec an, unum graece adolescens vel ad. Id odio scae has, iudico euismod atomorum ius ea, cum ea honestatis quaerendum theophrastus. Mea doming reprehendunt ex, cu eum civibus assentior posidonium. Quo etiam pertinax ex, te eros repudiandae cu. Accu aliquando nec an, unum graece adolescens vel ad. Id odio scae honestatis quaerendum theophrastus. Mea</p>
        <p class="letter__paragraph">Lorem ipsum dolor sit amet, an vel recteque dissentiet, detracto albucius platonem ex vel, eros repudiandae cu. Accu aliquando nec an, unum graece adolescens vel ad. Id odio scae has, iudico euismod atomorum ius ea, cum ea honestatis quaerendum theophrastus. Mea honestatis quaerendum theophrastus. Mea</p>

        <div class="signoff">
          <p class="signoff__closing">Kind Regards</p>
          <p class="signoff__name">Daniel Whitford</p>
          <p class="signoff__title">Chief Alchemist</p>
          <div class="signoff__signature" role="img" aria-label="Handwritten signature"></div>
        </div>
      </article>
    </section>

    <footer class="footer">
      <p class="footer__line">P : (877) 555-0192 | M : (919) 555-0147 | W : www.tidewallco.com</p>
      <p class="footer__line">A : PO Box 406 | Cary, NC 27519</p>
      <p class="footer__line">North Carolina | South Carolina | Virginia</p>
    </footer>
  </main>
</body>
</html>
```